A land page lead collector for people who want to reduce there postage costs

We are looking to create a single page website landing page to collect leads of people who want to reduce there postage costs.

The form should basically ask:

Name:
Business Name:
Address:
Town:
Post Code:
Email:
Phone:
Letter Volume Per Week:
Parcel Volume Per Week:

We should basically be advertising cheaper postage costs.

We will not be showing prices on this website we will just be collecting the leads.

Our competition website is as follows https://mailfernquest.com

But we are not a online service. This is just a collector to get leads of people who want to save money on there postage costs.
Updates

Target Market(s)

Small and medium sized enterprises

Industry/Entity Type

Advertising

Number of Pages Required

1 page

Colors
ec2027
0356a4

Requirements
Must have
• Form above the fold of the page
Nice to have
• Colour red and blue.
• Parallax design would be nice.

```html
<!DOCTYPE html>
<html lang="en">
<head>
<meta charset="utf-8">
<title>Reduce Your Postage Charge</title>
<link rel="stylesheet" href="https://fonts.googleapis.com/css2?family=Montserrat:wght@400;500;700;800&family=Open+Sans:wght@400;600&family=Lora:ital@1&display=swap">
<style>
  :root {
    --hero-deep: #7c0d14;
    --hero-mid: #a9161f;
    --hero-warm: #c9451f;
    --accent: #f0344a;
    --white: #ffffff;
    --panel-grey: #f2f2f2;
    --field-grey: #f1f1f1;
    --field-border: #dcdcdc;
    --ink: #1e1e1e;
    --muted: #9a9a9a;
    --link: #555555;
  }
  * { box-sizing: border-box; margin: 0; padding: 0; }
  html, body { width: 1200px; height: 687px; overflow: hidden; }
  body { font-family: "Open Sans", Arial, sans-serif; color: var(--white); }

  .hero { position: relative; width: 1200px; height: 687px; overflow: hidden; }
  .hero-backdrop {
    position: absolute;
    inset: 0;
    background:
      radial-gradient(ellipse 520px 380px at 330px 120px, rgba(214, 92, 40, 0.75), transparent 70%),
      radial-gradient(ellipse 420px 520px at 560px 420px, rgba(232, 58, 70, 0.55), transparent 70%),
      radial-gradient(ellipse 500px 400px at 1100px 200px, rgba(200, 30, 48, 0.6), transparent 70%),
      linear-gradient(160deg, var(--hero-warm) 0%, var(--hero-mid) 45%, var(--hero-deep) 100%);
  }
  .hero-rule {
    position: absolute;
    left: 0; right: 0; top: 15px;
    height: 1px;
    background: rgba(255, 255, 255, 0.12);
  }

  .hero-copy { position: absolute; left: 165px; top: 126px; width: 430px; }
  .eyebrow {
    font-family: "Lora", Georgia, serif;
    font-style: italic;
    font-size: 13px;
    margin-bottom: 24px;
  }
  .headline {
    font-family: "Montserrat", Arial, sans-serif;
    font-weight: 800;
    font-size: 54px;
    line-height: 56px;
    letter-spacing: 1px;
    text-transform: uppercase;
  }
  .intro {
    margin-top: 32px;
    width: 420px;
    font-size: 15px;
    line-height: 21px;
  }
  .actions { display: flex; gap: 17px; margin-top: 32px; }
  .btn {
    display: inline-flex;
    align-items: center;
    justify-content: center;
    height: 42px;
    font-family: "Montserrat", Arial, sans-serif;
    font-weight: 700;
    font-size: 9px;
    letter-spacing: 0.8px;
    text-transform: uppercase;
    text-decoration: none;
  }
  .btn-solid { width: 141px; background: var(--white); color: var(--ink); }
  .btn-outline { width: 118px; border: 2px solid var(--white); color: var(--white); }

  .lead-card {
    position: absolute;
    left: 614px; top: 110px;
    width: 424px; height: 460px;
    background: var(--white);
    color: var(--ink);
  }
  .lead-card-header {
    height: 56px;
    background: var(--panel-grey);
    padding: 21px 0 0 23px;
    font-family: "Montserrat", Arial, sans-serif;
    font-weight: 500;
    font-size: 17px;
    text-transform: uppercase;
  }
  .lead-fields {
    display: grid;
    grid-template-columns: 184px 184px;
    column-gap: 11px;
    row-gap: 10px;
    padding: 12px 0 0 20px;
  }
  .field {
    display: block;
    width: 100%;
    height: 34px;
    background: var(--field-grey);
    border: 1px solid var(--field-border);
    padding: 0 10px;
    font-family: "Open Sans", Arial, sans-serif;
    font-size: 11px;
    color: var(--ink);
  }
  .field::placeholder { color: var(--muted); }
  .field-wide { grid-column: 1 / 3; }
  textarea.field { height: 52px; padding-top: 8px; resize: vertical; }
  .lead-card-footer {
    position: absolute;
    left: 0; bottom: 0;
    width: 100%; height: 84px;
    background: var(--panel-grey);
    display: flex;
    align-items: center;
    justify-content: space-between;
    padding: 0 23px;
  }
  .btn-submit {
    width: 142px; height: 42px;
    border: 0;
    background: var(--accent);
    color: var(--white);
    font-family: "Montserrat", Arial, sans-serif;
    font-weight: 700;
    font-size: 9px;
    letter-spacing: 0.5px;
    text-transform: uppercase;
  }
  .legal-links { font-size: 11px; color: var(--link); }
  .legal-links a { color: var(--link); text-decoration: none; }
  .legal-links .divider { display: inline-block; width: 1px; height: 14px; background: var(--link); vertical-align: middle; margin: 0 6px; }
</style>
</head>
<body>
  <section class="hero">
    <div class="hero-backdrop" role="img" aria-label="Red-tinted photo of a hand holding a smartphone"></div>
    <div class="hero-rule"></div>

    <div class="hero-copy">
      <p class="eyebrow">Try it Now</p>
      <h1 class="headline">Reduce<br>Your<br>Postage<br>Charge</h1>
      <p class="intro">Lorem ipsum dolor sit amet, consectetuer adipiscing elit, sed diam nonummy nibh euismod tincidunt ut laoreet dolore magna aliquam erat volutpat.</p>
      <div class="actions">
        <a class="btn btn-solid" href="#">Know More</a>
        <a class="btn btn-outline" href="#">Contact Us</a>
      </div>
    </div>

    <form class="lead-card">
      <div class="lead-card-header">Get in Touch</div>
      <div class="lead-fields">
        <input class="field" type="text" placeholder="Your name...">
        <input class="field" type="text" placeholder="Business name...">
        <input class="field field-wide" type="text" placeholder="Address...">
        <input class="field" type="text" placeholder="Town...">
        <input class="field" type="text" placeholder="Post code...">
        <input class="field" type="email" placeholder="Your email...">
        <input class="field" type="tel" placeholder="Phone number (optional)...">
        <input class="field" type="number" placeholder="Letters per week...">
        <input class="field" type="number" placeholder="Parcels per week...">
        <textarea class="field field-wide" placeholder="Message..."></textarea>
      </div>
      <div class="lead-card-footer">
        <button class="btn-submit" type="submit">Sign Up Now!</button>
        <p class="legal-links"><a href="#">Privacy Policy</a><span class="divider"></span><a href="#">Terms &amp; Conditions</a></p>
      </div>
    </form>
  </section>
</body>
</html>
```